Market Lantern Fair needs a poster design

We need a poster to promote our showcase to both potential local vendors now, and visitors to the show on the actual day. See attached files and also checkout our plain square page - "Market Lantern Fair" for more information. Please state that booths are 8' (don't say 8' by 8'). See attached info that we have done so far, but we need something more professional. Ensure you use the Rest Easy Buy Nearby logo. The poster should be printable on both letter (8 1/2" by 11') and ledger sizes (11" by 17"). I have attached a sample of the poster from our last event - the Dwelling Expo 2013. I want the new poster similar to this (doesn't have to be exact, this is just to give you an idea.. The grand prize this time is a trip for two! The contact info has changed too, please note it on the new poster. I am no longer with my last company (BVC, Larchmere Campus), so don't put that on the new poster. Thank you. You can email me with any questions. marketlanternfair@mailbrook.example

Target Market(s)

Vendors for booth rentals. The community to visit the show.... They need to know that someone is going to win a trip for 2. We also have food, beer and wine sampling.

Industry/Entity Type

It Company

Font styles to use
Sans Serif

Requirements
Must have
• Rest easy buy nearby logo. Location. Email. Phone numbers. "Like our plain square page - "Market Lantern Fair". Poster is meant to attract business vendors now and to advertise the show to the public to attend in April. Must be able to print the poster on both letter size and ledger size paper. Need it in jpg too for plain square uploads
Nice to have
• If it fits would be nice to say first of its kind in North Grenville
• First annual Market Lantern Fair
Should not have
• Not too wordy.... Can't be confusing. Don't really need booth size on poster. Just state that both booths and marketplace tables are available. Not too many colours. We will be putting the poster in the newspaper in black and white only!

```html
<!DOCTYPE html>
<html lang="en">
<head>
<meta charset="utf-8">
<title>Market Lantern Fair – 1st Annual Poster</title>
<link rel="stylesheet" href="https://fonts.googleapis.com/css2?family=Josefin+Sans:wght@600;700&family=Roboto:ital,wght@0,400;0,700;1,700&family=Open+Sans:wght@400;600&display=swap">
<style>
  :root {
    --green: #0d7a42;
    --green-soft: #6f9f7c;
    --green-pale: #e6efe3;
    --title-tint: #c9d8cb;
    --grey: #5e5f61;
    --grey-light: #77787a;
    --white: #ffffff;
  }
  * { margin: 0; padding: 0; box-sizing: border-box; }
  html, body { width: 900px; height: 1200px; overflow: hidden; background: var(--white); }
  .poster {
    position: relative; width: 900px; height: 1200px; overflow: hidden;
    font-family: "Roboto", Arial, sans-serif; color: var(--grey);
  }
  .poster p, .poster div { white-space: nowrap; }
  .burst {
    position: absolute; inset: 352px 0 0 0;
    background: radial-gradient(circle at 50% 45%, var(--white) 0%, #f3f7f1 40%, var(--green-pale) 100%);
  }
  .masthead {
    position: absolute; left: 0; top: 0; width: 900px; height: 342px;
    background: var(--green);
  }
  .masthead-rule {
    position: absolute; left: 0; top: 342px; width: 900px; height: 12px; background: var(--grey);
  }
  .badge {
    position: absolute; left: 14px; top: 110px; width: 166px; height: 220px;
    display: flex; flex-direction: column; align-items: center; justify-content: center;
    color: var(--white); font-family: "Open Sans", Arial, sans-serif; font-weight: 600;
    text-align: center; line-height: 1.05;
  }
  .badge-big { font-size: 38px; }
  .badge-small { font-size: 20px; margin: 8px 0; }
  .title { position: absolute; left: 190px; width: 690px; text-align: center;
    font-family: "Josefin Sans", "Century Gothic", sans-serif; font-weight: 700; line-height: 1; }
  .title-edition { top: 42px; font-size: 64px; color: var(--title-tint); letter-spacing: 3px; }
  .title-name { color: var(--white); text-shadow: 3px 3px 0 rgba(0,0,0,0.25); }
  .title-line1 { top: 132px; font-size: 68px; }
  .title-line2 { top: 215px; font-size: 110px; letter-spacing: 30px; padding-left: 30px; }
  .center { position: absolute; left: 0; width: 900px; text-align: center; font-weight: 700; }
  .venue { top: 380px; font-size: 40px; }
  .date { top: 440px; font-size: 48px; color: var(--green); line-height: 1.12; }
  .admission { top: 553px; font-size: 70px; letter-spacing: 2px; }
  .ribbon { position: absolute; left: 0; top: 640px; width: 900px; height: 145px; }
  .ribbon-text {
    position: absolute; left: 95px; top: 654px; width: 710px; text-align: center;
    font-family: "Josefin Sans", "Century Gothic", sans-serif; font-weight: 700;
    color: var(--white); font-size: 44px; line-height: 1.05;
  }
  .ribbon-text em { font-style: italic; font-size: 40px; }
  .features {
    position: absolute; left: 82px; top: 800px; list-style: none;
    font-family: "Open Sans", Arial, sans-serif; font-size: 34px; color: var(--grey-light); line-height: 37px;
    white-space: nowrap;
  }
  .features li::before { content: "•"; color: var(--green-soft); font-size: 22px; margin-right: 16px; vertical-align: 4px; }
  .booths { top: 998px; font-size: 48px; color: var(--green); font-style: italic; }
  .book { top: 1048px; font-size: 50px; font-style: italic; }
  .phone { position: absolute; left: 22px; top: 1107px; font-size: 58px; font-weight: 700; letter-spacing: 1px; }
  .email { position: absolute; left: 22px; top: 1163px; font-size: 19px; font-weight: 700; color: var(--green); }
  .social { position: absolute; left: 450px; top: 1115px; display: flex; align-items: center; gap: 10px;
    font-size: 31px; }
  .social-square { width: 72px; height: 66px; border-radius: 10px; background: var(--green);
    border: 3px solid var(--green-soft); }
</style>
</head>
<body>
<main class="poster">
  <div class="burst" role="img" aria-label="Soft pale green sunburst background"></div>

  <header class="masthead">
    <div class="badge">
      <span class="badge-big">REST<br>EASY</span>
      <span class="badge-small">AND ...</span>
      <span class="badge-big">BUY<br>NEARBY</span>
    </div>
    <div class="title title-edition">1ST ANNUAL</div>
    <div class="title title-name title-line1">MARKET LANTERN</div>
    <div class="title title-name title-line2">FAIR</div>
  </header>
  <div class="masthead-rule"></div>

  <p class="center venue">Larkspur Hollow Civic Centre</p>
  <p class="center date">April 18th 2015<br>9am to 3pm</p>
  <p class="center admission">•FREE ADMISSION•</p>

  <svg class="ribbon" viewBox="0 0 900 145" aria-hidden="true">
    <polygon points="0,35 150,35 150,140 0,140 45,88" fill="#6f9f7c"/>
    <polygon points="900,35 750,35 750,140 900,140 855,88" fill="#6f9f7c"/>
    <polygon points="8,43 145,43 145,132 8,132 52,88" fill="#0d7a42"/>
    <polygon points="892,43 755,43 755,132 892,132 848,88" fill="#0d7a42"/>
    <polygon points="95,105 150,140 150,105" fill="#3c5a45"/>
    <polygon points="805,105 750,140 750,105" fill="#3c5a45"/>
    <rect x="90" y="0" width="720" height="110" fill="#6f9f7c"/>
    <rect x="97" y="7" width="706" height="96" fill="#0d7a42"/>
  </svg>
  <div class="ribbon-text">GRAND PRIZE<br>TRIP FOR 2 <em>to</em> VEGAS</div>

  <ul class="features">
    <li>Home Services, Sales &amp; Renovations</li>
    <li>Local Dining and Confectionaries</li>
    <li>Healthy Active Living Services</li>
    <li>Weddings – Planning/Caterers/Decor</li>
    <li>Artisans &amp; One of a Kind Creations</li>
  </ul>

  <p class="center booths">8’ BOOTHS</p>
  <p class="center book">BOOK YOUR BOOTH NOW!</p>

  <p class="phone">613.555.0148</p>
  <p class="email">marketlanternfair@mailbrook.example</p>
  <div class="social"><span class="social-square"></span><span>: Market Lantern Fair</span></div>
</main>
</body>
</html>
```